Webpage Needed for Bright Harbor Wiring Electrical and Security

We need a web design for our company showing people we arent just a small business. We want to look big so people can trust us. I would like information from my business cards on the page. example, we do all house rennovations, construction, commercial, 24 hour emergency service, new installations, repairs, maintenance, home theatre and so on...

I would also like images from my facebook on the page and linked. facebook.com/brightharborwiring

Target Market(s)

builders, residents,

Industry/Entity Type

Business

Number of Pages Required

1 page

Font styles to use
Other font styles liked:
• Juice bold

Requirements
Must have
• colours the same as the logo. background must be white. also the font must be Juice Bold which is the font of the logo
Should not have
• black as the background

```html
<!DOCTYPE html>
<html lang="en">
<head>
<meta charset="utf-8">
<title>Bright Harbor Wiring Electrical and Security</title>
<link rel="stylesheet" href="https://fonts.googleapis.com/css2?family=Aldrich&family=Open+Sans:wght@400;600&display=swap">
<style>
  :root {
    --blue: #3cb4e6;
    --blue-deep: #1f9fd6;
    --orange: #f08b3c;
    --ink: #4a4f5a;
    --muted: #9ba1ab;
    --soft-bg: #f4f5fa;
    --line: #e3e8ee;
    --white: #ffffff;
    --hero-dark: #2b2a2c;
  }
  * { box-sizing: border-box; margin: 0; padding: 0; }
  html, body { width: 1200px; height: 2707px; overflow: hidden; }
  body {
    position: relative;
    background: var(--white);
    font-family: "Aldrich", "Open Sans", sans-serif;
    color: var(--ink);
  }
  .abs { position: absolute; }
  .center-x { left: 0; width: 1200px; text-align: center; }

  /* Hero */
  .hero {
    position: absolute; left: 0; top: 0; width: 1200px; height: 535px;
    background:
      radial-gradient(ellipse at 50% 85%, rgba(120,110,105,.55), transparent 60%),
      linear-gradient(180deg, #3a3436 0%, #5b524f 40%, #6f6560 70%, #3d3838 100%);
  }
  .nav { position: absolute; left: 200px; top: 40px; display: flex; gap: 18px; font-size: 18px; color: var(--white); }
  .nav a { color: var(--white); text-decoration: none; }
  .nav .active { border-bottom: 2px solid var(--white); padding-bottom: 3px; }
  .call { position: absolute; left: 830px; top: 30px; color: var(--white); }
  .call-label { font-size: 13px; letter-spacing: 1px; }
  .call-number { font-size: 30px; margin-top: 2px; }
  .hero-links { position: absolute; inset: 0; }
  .feature { position: absolute; width: 260px; text-align: center; color: var(--white); font-size: 20px; letter-spacing: 1px; }
  .feature-icon { display: block; margin: 8px auto 0; }
  .diamond {
    position: absolute; left: 455px; top: 150px; width: 220px; height: 220px;
    transform: rotate(45deg); background: var(--white); border: 4px solid #3a3a3a;
  }
  .brand-mark { position: absolute; left: 440px; top: 205px; width: 250px; text-align: center; color: var(--blue-deep); font-family: "Aldrich", sans-serif; }
  .brand-name { font-size: 34px; line-height: 1.05; }
  .brand-sub { font-size: 15px; margin-top: 8px; }

  /* Section headings */
  .section-title { font-size: 30px; color: var(--blue); letter-spacing: 1px; }
  .title-ring { width: 14px; height: 14px; border: 2px solid var(--blue); border-radius: 50%; margin: 0 auto; }

  /* About */
  .about { position: absolute; left: 0; top: 535px; width: 1200px; height: 266px; background: var(--soft-bg); }
  .about-text { position: absolute; left: 200px; top: 122px; width: 800px; text-align: center; font-size: 13.5px; line-height: 24px; color: var(--muted); letter-spacing: .8px; }
  .read-more { position: absolute; top: 224px; font-size: 11px; color: var(--muted); letter-spacing: 1px; }

  /* Services */
  .services-box { position: absolute; left: 151px; top: 950px; width: 898px; height: 257px; border: 1px solid var(--line); }
  .service-col { position: absolute; top: 24px; list-style: none; }
  .service-col li { display: flex; align-items: center; gap: 14px; height: 42.5px; font-size: 15px; color: var(--ink); letter-spacing: 1px; }
  .col-divider { position: absolute; top: 22px; width: 1px; height: 210px; background: var(--line); }

  /* Partners */
  .partners { position: absolute; left: 176px; top: 1426px; width: 853px; height: 187px; display: grid; grid-template-columns: repeat(4, 1fr); grid-template-rows: 1fr 1fr; }
  .partner { display: flex; align-items: center; justify-content: center; border-right: 1px solid var(--line); border-bottom: 1px solid var(--line); }
  .partner:nth-child(4n) { border-right: none; }
  .partner:nth-child(n+5) { border-bottom: none; }
  .badge { width: 150px; height: 44px; background: #c9ccd1; border-radius: 4px; }
  .badge.round { width: 120px; height: 54px; border-radius: 50%; }
  .badge.slim { height: 30px; }

  /* Testimonials */
  .testimonials { position: absolute; left: 0; top: 1723px; width: 1200px; height: 285px; background: var(--soft-bg); }
  .quote-mark { position: absolute; left: 306px; top: 100px; font-size: 40px; color: var(--blue); line-height: 1; }
  .quote-text { position: absolute; left: 350px; top: 106px; width: 560px; font-size: 17px; line-height: 28px; color: var(--ink); text-align: center; }
  .dots { position: absolute; top: 242px; left: 0; width: 1200px; display: flex; justify-content: center; gap: 7px; }
  .dot { width: 12px; height: 12px; border-radius: 50%; border: 1.5px solid var(--muted); }
  .dot.on { background: var(--orange); border-color: var(--orange); }

  /* Map */
  .map { position: absolute; left: 0; top: 2125px; width: 1200px; height: 270px; background: linear-gradient(135deg, #e9eaec, #dfe1e3 50%, #eceded); }

  /* Footer */
  .footer { position: absolute; left: 0; top: 2395px; width: 1200px; height: 312px; background: var(--blue); color: var(--white); }
  .footer-badge { position: absolute; left: 520px; top: -80px; width: 160px; height: 160px; border-radius: 50%; background: var(--white); display: flex; flex-direction: column; align-items: center; justify-content: center; color: var(--blue-deep); text-align: center; }
  .footer-badge .brand-name { font-size: 22px; }
  .footer-badge .brand-sub { font-size: 10px; margin-top: 4px; }
  .avail { top: 95px; font-size: 16px; letter-spacing: 1px; }
  .contact-name { top: 124px; font-size: 12px; letter-spacing: 1px; font-family: "Open Sans", sans-serif; font-weight: 600; }
  .contact-line { position: absolute; font-family: "Open Sans", sans-serif; font-size: 12px; }
  .contact-line .label { color: #d8f0fb; display: inline-block; width: 70px; text-align: right; margin-right: 16px; }
  .socials { position: absolute; top: 210px; left: 0; width: 1200px; display: flex; justify-content: center; gap: 14px; }
  .social { width: 22px; height: 22px; border-radius: 50%; background: var(--white); }
  .copyright { top: 258px; font-family: "Open Sans", sans-serif; font-size: 12px; font-style: italic; }
</style>
</head>
<body>

<header class="hero" role="img" aria-label="Photo of an electrical and audio showroom interior">
</header>
<nav class="nav">
  <a class="active" href="#">Home</a>
  <a href="#">about us</a>
  <a href="#">services</a>
  <a href="#">contact</a>
</nav>
<div class="call">
  <div class="call-label">CALL NOW</div>
  <div class="call-number">+0400128650</div>
</div>

<svg class="hero-links abs" width="1200" height="535" viewBox="0 0 1200 535" fill="none" stroke="#ffffff" stroke-width="3" stroke-linecap="round">
  <path d="M470 180 C430 150 410 160 395 185"/>
  <path d="M395 185 l2 -12 M395 185 l11 -4"/>
  <path d="M660 180 C700 145 740 150 770 170"/>
  <path d="M770 170 l-11 -4 M770 170 l-3 -11"/>
  <path d="M470 335 C430 355 415 350 400 335"/>
  <path d="M400 335 l10 4 M400 335 l0 11"/>
  <path d="M660 335 C700 360 730 355 755 335"/>
  <path d="M755 335 l-11 3 M755 335 l1 11"/>
</svg>

<div class="feature" style="left:255px; top:180px;">CONSTRUCTION
  <svg class="feature-icon" width="70" height="50" viewBox="0 0 70 50" role="img" aria-label="Hard hat icon"><rect x="8" y="8" width="54" height="38" rx="19" fill="#f6a623"/></svg>
</div>
<div class="feature" style="left:698px; top:165px;">COMMERCIAL
  <svg class="feature-icon" width="56" height="80" viewBox="0 0 56 80" role="img" aria-label="Office building icon"><rect x="6" y="4" width="44" height="72" fill="#3cb4e6"/></svg>
</div>
<div class="feature" style="left:242px; top:342px;">MAINTENANCE
  <svg class="feature-icon" width="76" height="76" viewBox="0 0 76 76" role="img" aria-label="Crossed tools icon"><circle cx="38" cy="38" r="32" fill="#3cb4e6"/></svg>
</div>
<div class="feature" style="left:715px; top:342px;">NEW INSTALLATIONS
  <svg class="feature-icon" width="70" height="70" viewBox="0 0 70 70" role="img" aria-label="Gear icon"><circle cx="35" cy="35" r="28" fill="#f6a623"/><circle cx="35" cy="35" r="10" fill="#6f6560"/></svg>
</div>

<div class="diamond"></div>
<div class="brand-mark">
  <div class="brand-name">Bright Harbor<br>Wiring</div>
  <div class="brand-sub">electrical and security</div>
</div>

<!-- About -->
<section class="about">
  <h2 class="section-title abs center-x" style="top:45px;">ABOUT US</h2>
  <div class="abs center-x" style="top:87px;"><div class="title-ring"></div></div>
  <p class="about-text">WE COVER ALL NEW ELECTRICAL INSTALLATIONS, REPAIRS, MAINTENANCE, RENOVATIONS/EXTENSIONS, RE-WIRING, HOME THEATRE, SURROUND SOUND, WALL TV'S, ELECTRIC HOT WATER, STOVES, COOKTOPS, LIGHTING, CEILING FANS, DATA, TELEPHONE AND SECURITY SYSTEMS.</p>
  <div class="read-more center-x">— READ MORE —</div>
</section>

<!-- Services -->
<h2 class="section-title abs center-x" style="top:858px;">OUR SERVICES</h2>
<div class="abs center-x" style="top:906px;"><div class="title-ring"></div></div>

<svg width="0" height="0" style="position:absolute">
  <symbol id="tick" viewBox="0 0 20 20">
    <circle cx="10" cy="10" r="10" fill="#3cb4e6"/>
    <path d="M5.5 10.5 l3 3 l6 -7" fill="none" stroke="#ffffff" stroke-width="2.4" stroke-linecap="round" stroke-linejoin="round"/>
  </symbol>
</svg>

<div class="services-box">
  <ul class="service-col" style="left:28px;">
    <li><svg width="18" height="18"><use href="#tick"/></svg>24 / 7</li>
    <li><svg width="18" height="18"><use href="#tick"/></svg>HOME THEATRE</li>
    <li><svg width="18" height="18"><use href="#tick"/></svg>ELECTRIC HOT WATER</li>
    <li><svg width="18" height="18"><use href="#tick"/></svg>NEW INTSALLATIONS</li>
    <li><svg width="18" height="18"><use href="#tick"/></svg>TESTING AND TAGGING</li>
  </ul>
  <div class="col-divider" style="left:308px;"></div>
  <ul class="service-col" style="left:340px;">
    <li><svg width="18" height="18"><use href="#tick"/></svg>SURROUND SOUND</li>
    <li><svg width="18" height="18"><use href="#tick"/></svg>MAINTENANCE</li>
    <li><svg width="18" height="18"><use href="#tick"/></svg>COOKTOPS</li>
    <li><svg width="18" height="18"><use href="#tick"/></svg>RENOVATIONS</li>
    <li><svg width="18" height="18"><use href="#tick"/></svg>LIGHTING</li>
  </ul>
  <div class="col-divider" style="left:610px;"></div>
  <ul class="service-col" style="left:642px;">
    <li><svg width="18" height="18"><use href="#tick"/></svg>RE-WIRING</li>
    <li><svg width="18" height="18"><use href="#tick"/></svg>REPAIRS</li>
    <li><svg width="18" height="18"><use href="#tick"/></svg>TELEPHONE</li>
    <li><svg width="18" height="18"><use href="#tick"/></svg>WALL TV,S</li>
    <li><svg width="18" height="18"><use href="#tick"/></svg>STOVES</li>
  </ul>
</div>

<!-- Partners -->
<h2 class="section-title abs center-x" style="top:1318px;">OUR PARTNERS</h2>
<div class="abs center-x" style="top:1369px;"><div class="title-ring"></div></div>
<div class="partners" aria-label="Partner badges">
  <div class="partner"><div class="badge"></div></div>
  <div class="partner"><div class="badge slim"></div></div>
  <div class="partner"><div class="badge slim"></div></div>
  <div class="partner"><div class="badge slim"></div></div>
  <div class="partner"><div class="badge"></div></div>
  <div class="partner"><div class="badge"></div></div>
  <div class="partner"><div class="badge round"></div></div>
  <div class="partner"><div class="badge slim"></div></div>
</div>

<!-- Testimonials -->
<section class="testimonials">
  <h2 class="section-title abs center-x" style="top:27px;">TESTIMONIALS</h2>
  <div class="abs center-x" style="top:75px;"><div class="title-ring"></div></div>
  <div class="quote-mark">&ldquo;</div>
  <p class="quote-text">Lorem ipsum dolor sit amet, consectetuer adipiscing elit, sed diam nonummy nibh euismod tincidunt ut laoreet dolore magna aliquam erat volutpat. Ut wisi enim ad minim veniam, quis nostrud exerci tation ullamcorper suscipit lobortis nisl ut aliquip ex ea commodo consequat.</p>
  <div class="dots"><span class="dot on"></span><span class="dot"></span><span class="dot"></span><span class="dot"></span></div>
</section>

<!-- Locate -->
<h2 class="section-title abs center-x" style="top:2037px;">LOCATE US</h2>
<div class="abs center-x" style="top:2086px;"><div class="title-ring"></div></div>
<div class="map" role="img" aria-label="Street map showing the business location"></div>

<!-- Footer -->
<footer class="footer">
  <div class="footer-badge">
    <div class="brand-name">Bright Harbor<br>Wiring</div>
    <div class="brand-sub">electrical and security</div>
  </div>
  <div class="abs center-x avail">WE ARE AVAILABLE 24/7</div>
  <div class="abs center-x contact-name">SAM TELLER</div>
  <div class="contact-line" style="left:450px; top:150px;"><span class="label">Say Hello:</span>+0400128650</div>
  <div class="contact-line" style="left:450px; top:172px;"><span class="label">Email:</span>sam@brightharborwiring.com.au</div>
  <div class="socials" aria-label="Social links">
    <span class="social"></span><span class="social"></span><span class="social"></span><span class="social"></span><span class="social"></span>
  </div>
  <div class="abs center-x copyright">© 2015 All rights reserved. brightharborwiring.com.au</div>
</footer>

</body>
</html>
```